Store Bill board

We have a 10' x 29' sign off of a major highway that we need a billboard designed for. We have had a few preliminary desgins but want something really eye catching as you have less than a second in many cases to catch people's eyes. We have different logos and pics that a designer can choose and design with. It has to also have a 'Visit Our Store' on the bottom right and corner with an arrow. We like the Locally Built , locally born logo but would want the font much bigger and the Colorado flag underneath bigger. We'd like to see our logo say 'custom electric bikes' underneath the GrivO-Rides logo rather than 'fat tire electric bikes'

```html
<!DOCTYPE html>
<html lang="en">
<head>
<meta charset="utf-8">
<title>GrivO-Rides Highway Billboard</title>
<link rel="stylesheet" href="https://fonts.googleapis.com/css2?family=Montserrat:wght@700;800;900&display=swap">
<style>
  :root {
    --orange: #f36f24;
    --black: #111111;
    --white: #ffffff;
    --shadow-grey: #d9d9d9;
    --flag-blue: #0f2f80;
    --flag-red: #d21f26;
    --flag-gold: #f7cf14;
    --page: #eef0f2;
  }
  * { margin: 0; padding: 0; box-sizing: border-box; }
  html, body {
    width: 1200px;
    height: 905px;
    overflow: hidden;
    background: var(--page);
    font-family: "Montserrat", Arial, sans-serif;
  }
  .billboard {
    position: absolute;
    left: 20px;
    top: 200px;
    width: 1160px;
    height: 505px;
    background: var(--white);
    overflow: hidden;
  }
  .billboard-art {
    position: absolute;
    inset: 0;
    width: 1160px;
    height: 505px;
  }
  .text {
    position: absolute;
    font-weight: 800;
    line-height: 1;
    white-space: nowrap;
  }
  .tagline-top {
    left: 750px;
    top: 25px;
    width: 395px;
    text-align: center;
    font-size: 28px;
    color: var(--white);
  }
  .headline-fat-tire {
    left: 765px;
    top: 96px;
    width: 250px;
    text-align: center;
    font-size: 46px;
    font-weight: 900;
    color: var(--white);
    letter-spacing: -1px;
  }
  .headline-electric {
    left: 730px;
    top: 172px;
    width: 415px;
    text-align: center;
    font-size: 48px;
    color: var(--orange);
  }
  .brand-name {
    left: 810px;
    top: 262px;
    width: 335px;
    text-align: center;
    font-size: 50px;
    font-weight: 900;
    color: var(--black);
    letter-spacing: -1px;
  }
  .brand-tagline {
    left: 810px;
    top: 322px;
    width: 335px;
    text-align: right;
    font-size: 13px;
    font-weight: 800;
    color: var(--orange);
  }
  .local-born,
  .local-built {
    left: 540px;
    width: 260px;
    text-align: center;
    font-size: 32px;
  }
  .local-born { top: 412px; color: var(--white); }
  .local-built { top: 456px; color: var(--orange); }
  .visit-store {
    position: absolute;
    left: 845px;
    top: 452px;
    width: 305px;
    height: 44px;
    display: flex;
    align-items: center;
    justify-content: center;
    gap: 12px;
  }
  .visit-store-label {
    font-size: 26px;
    font-weight: 800;
    line-height: 1;
    color: var(--white);
    white-space: nowrap;
  }
  .visit-store-arrow {
    width: 32px;
    height: 26px;
    flex: none;
  }
</style>
</head>
<body>
  <main class="billboard">
    <svg class="billboard-art" viewBox="0 0 1160 505" xmlns="http://www.w3.org/2000/svg">
      <defs>
        <linearGradient id="rider-photo-tones" x1="0" y1="0" x2="1" y2="1">
          <stop offset="0" stop-color="#a79a90"/>
          <stop offset="0.5" stop-color="#c98a5a"/>
          <stop offset="1" stop-color="#6e6660"/>
        </linearGradient>
      </defs>

      <polygon class="rider-photo" role="img"
        aria-label="Photo of a rider on an orange fat tire electric bike on a paved plaza"
        points="0,0 612,0 460,505 0,505" fill="url(#rider-photo-tones)"/>

      <polygon class="lightning-bolt" points="622,0 742,0 640,195 722,195 470,505 590,292 500,292"
        fill="var(--orange)" stroke="var(--white)" stroke-width="10" stroke-linejoin="miter"/>

      <polygon class="band-top" points="754,0 1160,0 1160,82 712,82" fill="var(--orange)"/>

      <polygon class="fat-tire-shadow" points="757,90 1023,90 1013,162 767,162" fill="var(--shadow-grey)"/>
      <rect class="fat-tire-badge" x="765" y="86" width="250" height="66" rx="6" fill="var(--black)"/>

      <g class="colorado-flag">
        <rect x="700" y="244" width="92" height="88" fill="var(--white)"/>
        <rect x="700" y="244" width="92" height="29" fill="var(--flag-blue)"/>
        <rect x="700" y="303" width="92" height="29" fill="var(--flag-blue)"/>
        <circle cx="735" cy="288" r="24" fill="none" stroke="var(--flag-red)" stroke-width="14"
          stroke-dasharray="122 29" transform="rotate(30 735 288)"/>
        <circle cx="735" cy="288" r="12" fill="var(--flag-gold)"/>
      </g>

      <polygon class="local-badge" points="560,392 786,392 832,452 790,505 482,505" fill="var(--black)"/>

      <polygon class="band-bottom" points="842,442 1160,442 1160,505 792,505" fill="var(--orange)"/>
    </svg>

    <p class="text tagline-top">CUSTOM ELECTRIC BIKES</p>
    <h1 class="text headline-fat-tire">FAT TIRE</h1>
    <h2 class="text headline-electric">ELECTRIC BIKES</h2>
    <p class="text brand-name">GrivO-Rides</p>
    <p class="text brand-tagline">CUSTOM ELECTRIC BIKES</p>
    <p class="text local-born">LOCALLY BORN</p>
    <p class="text local-built">LOCALLY BUILT</p>
    <div class="visit-store">
      <span class="visit-store-label">VISIT OUR STORE</span>
      <svg class="visit-store-arrow" viewBox="0 0 32 26" xmlns="http://www.w3.org/2000/svg" aria-hidden="true">
        <polygon points="0,9 17,9 17,0 32,13 17,26 17,17 0,17" fill="var(--white)"/>
      </svg>
    </div>
  </main>
</body>
</html>
```